BrivoMatex. Lantern for the Steady Growth. Business card

Professional business card for BrivoMatex (Lantern for the Steady Growth)
My rationale: Strategy-> Execution-> Results-> Value that lead to the BrivoMatex name: We put the Lantern for the Steady Growth.
We deliver value to our customers helping them at defining a good strategy (cyan arrow). 90% of well formulated strategies fail due to poor execution so we also consider strategical execution very important (green arrow). Due to the execution we obtain the results (blue arrow). Finally, the results provide feedback to redefine strategy, and the new strategy has to be executed and new results obtained providing new feedback and on and on. It's like a wheel that finally, must create corporate value: value for shareholders, staholders, employees, providers...-

Target Market(s)

CEOs and steering comitees , invewrnent funds

Industry/Entity Type

Business Consultant

Contact Information for Business Card

Tommaso Ferlini
CEO & Founder
tommaso.ferlini@brivomatex.example
Mobile: +34 611.205.938
www.brivomatex.example

Colors

Designer to choose colors to be used in the design.

Requirements
Nice to have
• Nice to hace the words: Strategy, execution, results
• Nice to vave the claim: Lantern for the Steady Growth
• The three colors should be shown:
• cyan for STRATEGY
• green for EXECUTION
• blue for RESULTS
Should not have
• Complete black background

```html
<!DOCTYPE html>
<html lang="en">
<head>
<meta charset="utf-8">
<title>BrivoMatex — Business Card</title>
<link rel="stylesheet" href="https://fonts.googleapis.com/css2?family=Open+Sans:wght@400;600;700&display=swap">
<style>
  :root {
    --brand-blue: #213b8c;
    --brand-green: #7cc242;
    --paper: #f6f6f4;
    --ink: #2a2a3a;
    --stage: #c9cbcf;
  }
  * { box-sizing: border-box; margin: 0; padding: 0; }
  html, body {
    width: 1200px; height: 857px; overflow: hidden;
    background: var(--stage);
    font-family: "Open Sans", Arial, sans-serif;
  }
  .stage {
    position: relative; width: 1200px; height: 857px;
    display: flex; align-items: center; justify-content: center; gap: 60px;
  }
  .card {
    position: relative; width: 520px; height: 336px;
    box-shadow: 0 6px 18px rgba(0,0,0,.18);
    overflow: hidden;
  }
  /* Front */
  .card-front { background: var(--paper); }
  .holder { position: absolute; left: 38px; top: 52px; }
  .holder-name {
    color: var(--brand-blue); font-weight: 600; font-size: 27px; line-height: 1.1;
    letter-spacing: .3px;
  }
  .holder-role {
    color: var(--brand-green); font-weight: 600; font-size: 16px; margin-top: 2px; margin-left: 4px;
  }
  .brand-front {
    position: absolute; right: 34px; top: 44px;
    display: flex; align-items: center; gap: 10px;
  }
  .brand-dot { width: 14px; height: 14px; border-radius: 50%; background: var(--brand-green); }
  .brand-word {
    color: var(--brand-blue); font-weight: 700; font-size: 31px; letter-spacing: -.3px;
  }
  .contacts {
    position: absolute; left: 44px; top: 198px; list-style: none;
  }
  .contacts li {
    display: flex; align-items: center; gap: 12px;
    font-size: 12.5px; color: var(--ink); height: 19px;
  }
  .contacts svg { width: 15px; height: 15px; flex: none; }
  .rule { position: absolute; left: 0; right: 0; top: 292px; height: 4px; background: var(--brand-green); }
  .band { position: absolute; left: 0; right: 0; top: 296px; bottom: 0; background: var(--brand-blue); }
  /* Back */
  .card-back { background: var(--brand-blue); color: #fff; }
  .brand-back {
    position: absolute; left: 0; right: 0; top: 118px;
    display: flex; align-items: center; justify-content: center; gap: 14px;
  }
  .brand-back .brand-dot { width: 20px; height: 20px; background: #fff; }
  .brand-back .brand-word { color: #fff; font-size: 52px; }
  .site {
    position: absolute; left: 0; right: 0; top: 222px; text-align: center;
    font-size: 17px; letter-spacing: 6px; font-weight: 400;
  }
</style>
</head>
<body>
<main class="stage">
  <section class="card card-front" aria-label="Business card front">
    <div class="holder">
      <p class="holder-name">Tommaso Ferlini</p>
      <p class="holder-role">CEO &amp; Founder</p>
    </div>
    <div class="brand-front">
      <span class="brand-dot"></span>
      <span class="brand-word">BrivoMatex</span>
    </div>
    <ul class="contacts">
      <li>
        <svg viewBox="0 0 16 16" fill="none" stroke="#213b8c" stroke-width="1.4"><rect x="4" y="1.5" width="8" height="13" rx="1.5"/><line x1="7" y1="12.3" x2="9" y2="12.3"/></svg>
        +34 611.205.938
      </li>
      <li>
        <svg viewBox="0 0 16 16" fill="none" stroke="#213b8c" stroke-width="1.3"><rect x="1.5" y="3.5" width="13" height="9"/><polyline points="1.5,3.5 8,9 14.5,3.5"/></svg>
        tommaso.ferlini@brivomatex.example
      </li>
      <li>
        <svg viewBox="0 0 16 16" fill="none" stroke="#213b8c" stroke-width="1.2"><circle cx="8" cy="8" r="6.5"/><ellipse cx="8" cy="8" rx="3" ry="6.5"/><line x1="1.5" y1="8" x2="14.5" y2="8"/><line x1="2.5" y1="5" x2="13.5" y2="5"/><line x1="2.5" y1="11" x2="13.5" y2="11"/></svg>
        www.brivomatex.example
      </li>
    </ul>
    <div class="rule"></div>
    <div class="band"></div>
  </section>

  <section class="card card-back" aria-label="Business card back">
    <div class="brand-back">
      <span class="brand-dot"></span>
      <span class="brand-word">BrivoMatex</span>
    </div>
    <p class="site">www.brivomatex.example</p>
  </section>
</main>
</body>
</html>
```